Crestline Lending Group Business Cards

We are looking to revamp the current business cards each of our locations uses. We are a lending company that specializes in personal loans, title loans, and tax services. We have locations in New Mexico, Texas, and Oklahoma.

We would like a cleaner, sleeker look while still highlighting what we offer. Title Loans, Personal Loans & Tax Services. We also want to include our referral fee somewhere on the card. We would like to see an English option as well as a Spanish option for the cards.

PLEASE NOTE: Some business cards do not include the employee's name but just the store's location, while others will include both.

These are double-sided business cards, and we would like to see proof if possible. I have included proofs of our current business cards for you to review below, as well as our company logo. Feel free to get creative with the logo, etc! Colors should match the logo; however, you do not need to use all of our logo colors if you don't want to.

```html
<!DOCTYPE html>
<html lang="en">
<head>
<meta charset="utf-8">
<title>Crestline Lending Group — Business Cards</title>
<link href="https://fonts.googleapis.com/css2?family=Montserrat:wght@400;500;700;800;900&display=swap" rel="stylesheet">
<style>
  :root {
    --green: #145232;
    --green-deep: #0f4428;
    --red: #c8192a;
    --white: #ffffff;
    --ink: #3d3d3d;
    --backdrop: #2a2a2a;
  }
  * { box-sizing: border-box; margin: 0; padding: 0; }
  html, body { width: 1200px; height: 1000px; overflow: hidden; }
  body {
    background: var(--backdrop);
    font-family: "Montserrat", sans-serif;
    position: relative;
  }
  .card {
    position: absolute;
    left: 220px;
    width: 760px;
    height: 434px;
    border-radius: 22px;
    overflow: hidden;
  }
  /* Back side: referral offer */
  .card-back { top: 50px; background: var(--green); }
  .card-back .rule {
    position: absolute; left: 0; right: 0; top: 232px;
    height: 2px; background: var(--red);
  }
  .card-back .brand {
    position: absolute; left: 0; right: 0; top: 104px;
    text-align: center; color: var(--white);
    font-weight: 700; font-size: 40px; letter-spacing: 0.5px;
  }
  .card-back .brand-url {
    position: absolute; left: 0; right: 0; top: 162px;
    text-align: center; color: var(--red);
    font-weight: 500; font-size: 17px; letter-spacing: 1px;
  }
  .card-back .refer-pill {
    position: absolute; left: 50%; top: 206px; transform: translateX(-50%);
    width: 340px; height: 54px;
    border: 2px solid var(--red); border-radius: 27px;
    background: var(--green);
    color: var(--white); font-weight: 800; font-size: 30px;
    display: flex; align-items: center; justify-content: center;
    letter-spacing: 1px;
  }
  .card-back .offer {
    position: absolute; left: 0; right: 0; top: 290px;
    text-align: center; color: var(--white);
    font-weight: 900; font-size: 44px; letter-spacing: 2px;
  }
  .card-back .offer .amount { color: var(--red); }

  /* Front side: contact */
  .card-front { top: 516px; background: var(--white); }
  .card-front .wave { position: absolute; inset: 0; }
  .card-front .brand-block {
    position: absolute; left: 40px; top: 100px; width: 330px; text-align: center;
  }
  .card-front .brand {
    color: var(--green); font-weight: 700; font-size: 34px; line-height: 1.15;
  }
  .card-front .brand-url {
    margin-top: 14px; color: var(--red);
    font-weight: 500; font-size: 16px; letter-spacing: 1px;
  }
  .card-front .divider {
    position: absolute; left: 400px; top: 70px;
    width: 1.5px; height: 190px; background: var(--green);
  }
  .card-front .contact {
    position: absolute; left: 432px; top: 78px; color: var(--ink);
  }
  .contact .name { font-weight: 900; font-size: 30px; color: var(--green); letter-spacing: 1px; }
  .contact .name .surname { color: var(--red); }
  .contact .role { font-size: 18px; margin-top: 2px; letter-spacing: 0.5px; }
  .contact .address { font-size: 18px; margin-top: 14px; line-height: 1.3; letter-spacing: 0.5px; }
  .contact .line { display: flex; align-items: center; gap: 10px; font-size: 18px; margin-top: 10px; letter-spacing: 0.3px; white-space: nowrap; }
  .contact .line + .line { margin-top: 4px; }
  .contact .line svg { width: 16px; height: 16px; flex: none; }
  .card-front .services {
    position: absolute; left: 40px; top: 382px;
    display: flex; gap: 18px; color: var(--white);
    font-size: 18px; letter-spacing: 0.8px;
  }
  .services li { list-style: none; display: flex; align-items: center; gap: 7px; }
  .services svg { width: 13px; height: 13px; }
</style>
</head>
<body>

<section class="card card-back" aria-label="Business card back">
  <div class="rule"></div>
  <div class="brand">Crestline Lending Group</div>
  <div class="brand-url">www.crestlinelending.com</div>
  <div class="refer-pill">Refer a Friend</div>
  <div class="offer">GET UP TO <span class="amount">$100</span></div>
</section>

<section class="card card-front" aria-label="Business card front">
  <svg class="wave" viewBox="0 0 760 434" preserveAspectRatio="none" aria-hidden="true">
    <path d="M0 322 Q 470 330 760 434 L0 434 Z" fill="var(--red)"/>
    <path d="M0 332 Q 460 340 730 434 L0 434 Z" fill="var(--green)"/>
  </svg>

  <div class="brand-block">
    <div class="brand">Crestline<br>Lending Group</div>
    <div class="brand-url">www.crestlinelending.com</div>
  </div>

  <div class="divider"></div>

  <div class="contact">
    <div class="name">JANE <span class="surname">DOE</span></div>
    <div class="role">Branch manager</div>
    <div class="address">418 Mesa Road, Suite C<br>Riverton, Texas 75012</div>
    <div class="line">
      <svg viewBox="0 0 16 16" aria-hidden="true"><path fill="var(--red)" d="M3 2l3 0 1 3-2 1.5c.8 1.8 2.2 3.2 4 4L10.5 8.5l3 1v3c0 .8-.7 1.5-1.5 1.5C6.5 14 2 9.5 2 4c0-.8.2-2 1-2z"/></svg>
      <span>(505) 555-0148</span>
    </div>
    <div class="line">
      <svg viewBox="0 0 16 16" aria-hidden="true"><rect x="1" y="3" width="14" height="10" rx="1" fill="var(--red)"/><path d="M1.5 3.5 8 9l6.5-5.5" fill="none" stroke="var(--white)" stroke-width="1.2"/></svg>
      <span>abcde@crestlinelending.com</span>
    </div>
  </div>

  <ul class="services">
    <li><svg viewBox="0 0 14 14" aria-hidden="true"><circle cx="7" cy="7" r="6" fill="none" stroke="var(--red)" stroke-width="1.5"/><path d="M4 7l2 2 4-4" fill="none" stroke="var(--red)" stroke-width="1.5"/></svg>Title Loans</li>
    <li><svg viewBox="0 0 14 14" aria-hidden="true"><circle cx="7" cy="7" r="6" fill="none" stroke="var(--red)" stroke-width="1.5"/><path d="M4 7l2 2 4-4" fill="none" stroke="var(--red)" stroke-width="1.5"/></svg>Personal Loans</li>
    <li><svg viewBox="0 0 14 14" aria-hidden="true"><circle cx="7" cy="7" r="6" fill="none" stroke="var(--red)" stroke-width="1.5"/><path d="M4 7l2 2 4-4" fill="none" stroke="var(--red)" stroke-width="1.5"/></svg>Tax Services</li>
  </ul>
</section>

</body>
</html>
```